Kelvo Tech Oz Business card revamp

We are looking to revamp our business card design. We are hoping to change our colours to dark navey blue, gray, white and black but are open to keeping the same if a good design is submited. We are after somthing a bit differnt not just boring business card. I have attached a copy of our current card. We Want to keep the same logo design which i have attached a few to hopfully help you in this process. We are after a design that can be personalized to separate 4 people

Colors
0455a3
ffffff
000000
cbcbcb

Requirements
Must have
• Kelvo Tech Logo, address 3/41 Mallory Court, Wexhill 4218, phone number, Name and position

```html
<!DOCTYPE html>
<html lang="en">
<head>
<meta charset="utf-8">
<title>Kelvo Tech Oz – Business Card</title>
<link rel="stylesheet" href="https://fonts.googleapis.com/css2?family=Open+Sans:wght@400;600;700&display=swap">
<style>
  :root {
    --stage: #2b2b2b;
    --card: #262626;
    --card-edge: #1a1a1a;
    --blue: #3b86d4;
    --orange: #e17a3c;
    --text: #e6e6e6;
    --muted: #cbcbcb;
  }
  * { margin: 0; padding: 0; box-sizing: border-box; }
  html, body { width: 1200px; height: 716px; overflow: hidden; background: var(--stage); }
  body { font-family: "Open Sans", sans-serif; position: relative; }

  .card {
    position: absolute;
    top: 208px;
    width: 520px;
    height: 300px;
    background: var(--card);
    border-radius: 18px;
    box-shadow: 0 4px 0 var(--card-edge), 0 14px 30px rgba(0,0,0,.45);
    overflow: hidden;
  }
  .card--front { left: 40px; }
  .card--back { left: 640px; }

  /* front */
  .brand {
    font-weight: 700;
    color: var(--blue);
    display: flex;
    align-items: center;
    gap: 12px;
    white-space: nowrap;
  }
  .brand__dot {
    width: 0.6em; height: 0.6em;
    border-radius: 50%;
    background: var(--orange);
  }
  .card--front .brand {
    position: absolute;
    left: 0; right: 0; top: 100px;
    justify-content: center;
    font-size: 50px;
  }
  .card--front .website {
    position: absolute;
    left: 0; right: 0; top: 200px;
    text-align: center;
    font-size: 16px;
  }
  .website { color: var(--orange); }

  /* back */
  .holder {
    position: absolute;
    left: 38px; top: 34px;
    padding-left: 22px;
  }
  .holder__bar {
    position: absolute;
    left: 0; top: 2px;
    width: 9px; height: 50px;
    background: var(--blue);
  }
  .holder__name { font-size: 26px; color: var(--text); font-weight: 400; line-height: 1.1; }
  .holder__name strong { font-weight: 700; }
  .holder__title { font-size: 14px; color: var(--blue); }

  .card--back .brand {
    position: absolute;
    right: 34px; top: 128px;
    font-size: 34px;
  }

  .contacts {
    position: absolute;
    left: 38px; top: 178px;
    list-style: none;
  }
  .contacts li {
    display: flex; align-items: center; gap: 10px;
    font-size: 15px; color: var(--text);
    height: 25px;
  }
  .contacts svg { width: 14px; height: 14px; fill: var(--blue); flex: none; }

  .rule {
    position: absolute;
    left: 0; top: 262px;
    width: 360px; height: 2px;
    background: var(--blue);
  }
  .card--back .website {
    position: absolute;
    right: 30px; top: 252px;
    font-size: 17px;
  }
</style>
</head>
<body>

<section class="card card--front" aria-label="Card front">
  <div class="brand"><span class="brand__dot"></span>Kelvo Tech</div>
  <div class="website">www.kelvotech.com.au</div>
</section>

<section class="card card--back" aria-label="Card back">
  <div class="holder">
    <span class="holder__bar"></span>
    <div class="holder__name">Your <strong>Name</strong></div>
    <div class="holder__title">Job Title</div>
  </div>

  <div class="brand"><span class="brand__dot"></span>Kelvo Tech</div>

  <ul class="contacts">
    <li>
      <svg viewBox="0 0 24 24" aria-hidden="true"><path d="M6.6 10.8a15.1 15.1 0 0 0 6.6 6.6l2.2-2.2a1 1 0 0 1 1-.25 11.4 11.4 0 0 0 3.6.57 1 1 0 0 1 1 1V20a1 1 0 0 1-1 1A17 17 0 0 1 3 4a1 1 0 0 1 1-1h3.5a1 1 0 0 1 1 1c0 1.25.2 2.45.57 3.57a1 1 0 0 1-.25 1z"/></svg>
      07 5550 1842
    </li>
    <li>
      <svg viewBox="0 0 24 24" aria-hidden="true"><path d="M2 5h20v14H2zm2 2v.5l8 5 8-5V7l-8 5z"/></svg>
      youremail@xyz.com
    </li>
    <li>
      <svg viewBox="0 0 24 24" aria-hidden="true"><path d="M12 2a7 7 0 0 0-7 7c0 5.2 7 13 7 13s7-7.8 7-13a7 7 0 0 0-7-7zm0 9.5A2.5 2.5 0 1 1 12 6.5a2.5 2.5 0 0 1 0 5z"/></svg>
      3/41 Mallory Court, Wexhill
    </li>
  </ul>

  <div class="rule"></div>
  <div class="website">www.kelvotech.com.au</div>
</section>

</body>
</html>
```